Corvint Property Management Vendor Recruiting Email

We need a digital flyer to email and post on Social media to attract new vendors to our website to apply to complete maintenance work on our clients homes. I have one flyer we had produced recently that we are un-happy with. It is attached.

The example given is what we do not want!! We do not want any of the pictures used from the existing one

Target Market(s)

Construction companies and handyman

Industry/Entity Type

Residential maintenance and repairs

Requirements
Must have
• Join our team as the header not become a vendor

```html
<!DOCTYPE html>
<html lang="en">
<head>
<meta charset="utf-8">
<title>Corvint Property Management – Join Our Team</title>
<link rel="stylesheet" href="https://fonts.googleapis.com/css2?family=Bebas+Neue&family=Barlow+Condensed:wght@400&family=Poppins:wght@400;500;600;700&display=swap">
<style>
  :root {
    --ink-dark: #24132f;
    --ink: #111111;
    --white: #ffffff;
    --sky: #5aa8de;
    --sky-deep: #4a9fd8;
    --plum: #9b5ba8;
    --tile: #f1f1f6;
    --rule: #b9b4c8;
  }
  * { margin: 0; padding: 0; box-sizing: border-box; }
  html, body { width: 966px; height: 1200px; overflow: hidden; background: var(--ink-dark); }
  .flyer { position: relative; width: 966px; height: 1200px; overflow: hidden; font-family: "Poppins", sans-serif; color: var(--ink); }
  .backdrop { position: absolute; inset: 0; }
  .abs { position: absolute; }

  .brand { left: 62px; top: 100px; width: 190px; text-align: center; color: var(--white); }
  .brand-mark { width: 34px; height: 34px; margin: 0 auto 12px; background: var(--sky); }
  .brand-name { font-family: "Poppins", sans-serif; font-weight: 600; font-size: 17px; line-height: 1.25; letter-spacing: 2px; text-transform: uppercase; }

  .headline { margin: 0; }
  .headline-small, .headline-big { display: block; position: absolute; font-family: "Bebas Neue", sans-serif; font-weight: 400; color: var(--white); line-height: 1; white-space: nowrap; }
  .headline-small { left: 48px; top: 240px; font-size: 112px; letter-spacing: 9px; }
  .headline-big { left: 46px; top: 336px; font-size: 250px; letter-spacing: 40px; }

  .req-title { left: 86px; top: 556px; font-family: "Bebas Neue", sans-serif; font-weight: 400; font-size: 57px; letter-spacing: 3px; color: var(--white); line-height: 1; }
  .req-sub { left: 86px; top: 604px; font-family: "Bebas Neue", sans-serif; font-size: 37px; letter-spacing: 10.5px; color: var(--white); line-height: 1; }

  .checklist { list-style: none; font-size: 14.5px; line-height: 1.12; }
  .checklist li { position: absolute; padding-left: 26px; }
  .checklist li svg { position: absolute; left: 0; top: 3px; width: 13px; height: 11px; }

  .stat-icon { position: absolute; }
  .stat-figure { left: 157px; top: 834px; font-weight: 600; font-size: 54px; line-height: 1; letter-spacing: -1px; }
  .stat-note { left: 157px; top: 889px; font-size: 11.5px; line-height: 1.15; }
  .stat-note b { font-weight: 700; }

  .volume-lead { left: 360px; top: 840px; font-weight: 600; font-size: 27px; line-height: 1; letter-spacing: 0.5px; }
  .volume-main { left: 358px; top: 872px; font-weight: 700; font-size: 35px; line-height: 1; letter-spacing: 0.3px; }

  .material-title { left: 157px; top: 957px; font-weight: 700; font-size: 20px; line-height: 1.05; letter-spacing: 0.3px; }
  .material-note { left: 157px; top: 1030px; font-size: 10px; line-height: 1.15; }

  .deposit-title { left: 461px; top: 960px; font-weight: 700; font-size: 28px; line-height: 1.05; letter-spacing: 0.3px; }
  .deposit-note { left: 461px; top: 1036px; font-size: 15.5px; line-height: 1; }

  .call { left: 68px; top: 1085px; display: flex; align-items: center; white-space: nowrap; }
  .call svg { width: 20px; height: 20px; margin-right: 12px; }
  .call-label { font-family: "Bebas Neue", sans-serif; font-size: 45px; letter-spacing: 3px; line-height: 1; margin-right: 12px; }
  .call-number { font-weight: 700; font-size: 42px; letter-spacing: 1.5px; color: var(--plum); line-height: 1; }

  .rule { left: 62px; top: 1131px; width: 545px; height: 1px; background: var(--rule); }
  .site { left: 66px; top: 1134px; display: flex; align-items: center; white-space: nowrap; }
  .site svg { width: 22px; height: 22px; margin-right: 12px; }
  .site-url { font-family: "Barlow Condensed", sans-serif; font-size: 38px; letter-spacing: 5.2px; color: var(--sky-deep); line-height: 1; }
</style>
</head>
<body>
<main class="flyer">
  <svg class="backdrop" width="966" height="1200" viewBox="0 0 966 1200">
    <defs>
      <linearGradient id="photo-tone" x1="0" y1="0" x2="0" y2="1">
        <stop offset="0" stop-color="#cfe3d6"/>
        <stop offset="0.3" stop-color="#b7a99a"/>
        <stop offset="0.5" stop-color="#8c6aa8"/>
        <stop offset="0.7" stop-color="#34407a"/>
        <stop offset="1" stop-color="#c9a57e"/>
      </linearGradient>
      <linearGradient id="side-fade" x1="0" y1="0" x2="0" y2="1">
        <stop offset="0" stop-color="#24132f"/>
        <stop offset="0.55" stop-color="#a98bb4"/>
        <stop offset="1" stop-color="#ffffff"/>
      </linearGradient>
      <linearGradient id="base-band" x1="0" y1="0" x2="1" y2="0">
        <stop offset="0" stop-color="#9b5ba8"/>
        <stop offset="1" stop-color="#4aa3dc"/>
      </linearGradient>
    </defs>
    <rect class="backdrop-dark" width="966" height="1200" fill="var(--ink-dark)"/>
    <polygon class="photo-worker" role="img" aria-label="Photo of a smiling tradesman in a yellow hard hat holding a cordless drill on a job site"
             points="229,0 966,0 966,1200 859,1200 521,547" fill="url(#photo-tone)"/>
    <polygon class="accent-wedge" points="521,0 776,0 649,262" fill="var(--ink-dark)"/>
    <polygon class="header-band" points="62,547 521,547 581,651 62,651" fill="var(--sky)"/>
    <rect class="side-fade" x="0" y="651" width="62" height="140" fill="url(#side-fade)"/>
    <polygon class="content-panel" points="62,651 581,651 859,1200 0,1200 0,790 62,790" fill="var(--white)"/>
    <line class="panel-edge" x1="780" y1="547" x2="652" y2="795" stroke="var(--sky)" stroke-width="3"/>
    <polygon class="tile" points="62,818 330,818 330,936 62,936" fill="var(--tile)"/>
    <polygon class="tile" points="341,818 663,818 712,936 341,936" fill="var(--tile)"/>
    <polygon class="tile" points="62,947 330,947 330,1066 62,1066" fill="var(--tile)"/>
    <polygon class="tile" points="341,947 724,947 784,1066 341,1066" fill="var(--tile)"/>
    <rect class="base-band" x="0" y="1187" width="866" height="13" fill="url(#base-band)"/>
  </svg>

  <div class="abs brand">
    <div class="brand-mark"></div>
    <div class="brand-name">Corvint<br>Property Management</div>
  </div>

  <h1 class="headline">
    <span class="headline-small">Join our</span>
    <span class="headline-big">Team</span>
  </h1>

  <h2 class="abs req-title">Requirements</h2>
  <div class="abs req-sub">To become a vendor</div>

  <ul class="checklist">
    <li style="left:94px;top:672px;"><svg viewBox="0 0 13 11"><path d="M1 6l4 4 7-9" fill="none" stroke="#111" stroke-width="2"/></svg>Auto insurance</li>
    <li style="left:94px;top:710px;"><svg viewBox="0 0 13 11"><path d="M1 6l4 4 7-9" fill="none" stroke="#111" stroke-width="2"/></svg>Certificate of<br>general liability<br>insurance</li>
    <li style="left:94px;top:776px;"><svg viewBox="0 0 13 11"><path d="M1 6l4 4 7-9" fill="none" stroke="#111" stroke-width="2"/></svg>Coverage area</li>
    <li style="left:274px;top:671px;"><svg viewBox="0 0 13 11"><path d="M1 6l4 4 7-9" fill="none" stroke="#111" stroke-width="2"/></svg>Workman’s compensation or<br>state issued exemption letter</li>
    <li style="left:274px;top:724px;"><svg viewBox="0 0 13 11"><path d="M1 6l4 4 7-9" fill="none" stroke="#111" stroke-width="2"/></svg>Drive licence or state issued<br>ID card</li>
    <li style="left:274px;top:777px;"><svg viewBox="0 0 13 11"><path d="M1 6l4 4 7-9" fill="none" stroke="#111" stroke-width="2"/></svg>Any specialty licenses</li>
  </ul>

  <svg class="stat-icon" style="left:90px;top:857px;" width="42" height="42" viewBox="0 0 42 42">
    <circle cx="21" cy="21" r="18.5" fill="none" stroke="#111" stroke-width="3"/>
    <path d="M13 21l6 6 10-12" fill="none" stroke="#111" stroke-width="3"/>
  </svg>
  <div class="abs stat-figure">95%</div>
  <p class="abs stat-note"><b>approval rating</b> on all<br>submitted estimates.</p>

  <div class="abs volume-lead">Guaranteed</div>
  <svg class="stat-icon" style="left:574px;top:830px;" width="54" height="48" viewBox="0 0 54 48">
    <g fill="none" stroke="#111" stroke-width="2.5" stroke-linejoin="round">
      <path d="M27 3L51 14 27 25 3 14z"/>
      <path d="M3 23l24 11 24-11"/>
      <path d="M3 32l24 11 24-11"/>
    </g>
  </svg>
  <div class="abs volume-main">Work Volume.</div>

  <svg class="stat-icon" style="left:80px;top:988px;" width="56" height="52" viewBox="0 0 56 52">
    <g fill="none" stroke="#111" stroke-width="2.5">
      <path d="M10 2h22l8 8v8"/>
      <path d="M10 2H4v48h18"/>
      <rect x="22" y="18" width="30" height="32" rx="3"/>
      <rect x="27" y="23" width="20" height="6"/>
      <path d="M27 34h5M35 34h5M43 34h4M27 40h5M35 40h5M43 40h4M27 45h5M35 45h5"/>
    </g>
  </svg>
  <h3 class="abs material-title">Material<br>Purchasing<br>Program</h3>
  <p class="abs material-note">to help vendors with low<br>capital or no or bad credit.</p>

  <svg class="stat-icon" style="left:356px;top:984px;" width="72" height="52" viewBox="0 0 72 52">
    <g fill="none" stroke="#111" stroke-width="2.5" stroke-linejoin="round">
      <rect x="2" y="12" width="46" height="30"/>
      <rect x="14" y="6" width="46" height="36"/>
      <rect x="24" y="2" width="46" height="48"/>
      <circle cx="50" cy="26" r="7"/>
      <path d="M8 28h8M8 34h4"/>
    </g>
  </svg>
  <h3 class="abs deposit-title">Weekly Secure<br>Direct Deposit</h3>
  <p class="abs deposit-note">with net 30 payment terms.</p>

  <div class="abs call">
    <svg viewBox="0 0 24 24"><path d="M6.6 10.8a15.1 15.1 0 0 0 6.6 6.6l2.2-2.2a1 1 0 0 1 1-.25 11.4 11.4 0 0 0 3.6.57 1 1 0 0 1 1 1V20a1 1 0 0 1-1 1A17 17 0 0 1 3 4a1 1 0 0 1 1-1h3.5a1 1 0 0 1 1 1c0 1.25.2 2.45.57 3.57a1 1 0 0 1-.25 1z" fill="#111"/></svg>
    <span class="call-label">Call us now!</span>
    <span class="call-number">555-013-4827</span>
  </div>
  <div class="abs rule"></div>
  <div class="abs site">
    <svg viewBox="0 0 24 24"><g fill="none" stroke="#4a9fd8" stroke-width="1.6"><circle cx="12" cy="12" r="10"/><ellipse cx="12" cy="12" rx="4.5" ry="10"/><path d="M2 12h20M4 6.5h16M4 17.5h16"/></g></svg>
    <span class="site-url">www.corvintproperty.com</span>
  </div>
</main>
</body>
</html>
```